Designing Systems Engineering

We need to design the look and feel for an innovation company with software products for solving complex IT problems following socio-technical theory thinking. The company is heavy in designing of complex systems (like an architect shop). The new design will form the foundation of our brand moving forward. We will approach software projects as if one is building a skyscraper or a bridge. We want to humanize technology and not the other way around. Our target groups will be healthcare and the environment. We will be able to take complex problems and turn them into amazing IT solutions that improve the quality of life for people.

Here are more fragments of ideas that can help:
===============

Motivation

The technology described in the application, coincides with “Steer-Through-Mesh” concept of Marvin Oldroyd, which suggests managing a business by managing an informational representation of it : Marvin had the following vision:

"Imagine an enterprise design model that defines the behavior of an entire business. Imagine making this model a part of the corporate informational infrastructure, implementing it on technology that connects all relevant sources and users of information and affords maximum sharing among all parts of the firm. Managers could respond to the read-outs appearing on the console, modifying the flight plan en route based on changes in external conditions, monitoring the performance of delegated responsibilities, sending coordinated directions to subsidiary functions, and experiencing exhilaration upon their execution. It constitutes institutional memory and intelligence, which augment management's ability to run the business”.

This product does what Mr. Oldroyd envisioned.

The Objective

QLT offers software products for the specification, construction, assembly, and ongoing management of a digital representation that is an exact mirror image of an enterprise. The main idea is the capability of managing the enterprise by managing an information technology representation of it through software. The idea is to manage the enterprise as a total system involving all aspects of operations. That makes the enterprise and all its information technology representation is inseparable. The implication is that the management of change at the business and IT infrastructure levels are unified. For example, by reconfiguring the information representation of the enterprise one can change business performance. By changing the configuration of the business representation one can actually change the organization’s ability to respond to internal and external events. Management leadership can act with the aid of technology to better respond and improve their ability to guide the organization. The knowledge management feature of the digital representation of the enterprise enables managers to monitor the impact of change and therefore help management assess risk and determine whether mitigating responses are necessary.

The technology and product defines a new approach for the design, implementation, and ongoing execution of software systems that are truly business-like rather than applications and workflows.

```html
<!DOCTYPE html>
<html lang="en">
<head>
<meta charset="utf-8">
<title>Meshworks</title>
<link rel="stylesheet" href="https://fonts.googleapis.com/css2?family=Marcellus&family=Open+Sans:ital,wght@0,300;0,400;0,600;0,700;1,700&display=swap">
<style>
:root{
  --blue:#3aaee3;
  --blue-deep:#2590c4;
  --ink:#2a2a2a;
  --dark:#2d2d2d;
  --darker:#222222;
  --black:#111111;
  --white:#ffffff;
  --muted:#bbbbbb;
  --text:#444444;
}
*{margin:0;padding:0;box-sizing:border-box}
html,body{width:1200px;height:3103px;overflow:hidden}
body{position:relative;font-family:"Open Sans",Arial,sans-serif;color:var(--text);background:var(--white)}
.abs{position:absolute}
.heading{font-family:"Marcellus",Georgia,serif;font-weight:400;letter-spacing:1px;text-align:center}

/* hero */
.hero-photo{left:0;top:0;width:1200px;height:707px;background:linear-gradient(100deg,#c9d3dc 0%,#b89a86 22%,#e7e3df 38%,#c8a48c 55%,#d9d8d6 70%,#8a6652 88%,#d7dbe0 100%)}
.site-nav{left:0;top:0;width:1200px;height:69px;background:var(--blue)}
.site-name{left:178px;top:14px;font-family:"Open Sans",Arial,sans-serif;font-size:30px;font-weight:400;color:var(--white);letter-spacing:.5px;white-space:nowrap}
.nav-list{left:520px;top:0;height:69px;display:flex;gap:30px;list-style:none;align-items:center}
.nav-list li{font-size:14px;color:var(--white);white-space:nowrap}
.hero-caption{left:183px;top:500px;width:317px}
.hero-title{background:rgba(20,20,20,.88);color:var(--white);font-family:"Marcellus",Georgia,serif;font-size:38px;padding:6px 14px;height:62px;letter-spacing:1px;white-space:nowrap}
.hero-text{background:var(--blue);color:var(--white);font-size:15px;line-height:23px;padding:12px 14px;height:128px}
.hero-arrow{left:500px;width:36px;height:40px;background:rgba(20,20,20,.88)}

/* what we do */
.services{left:0;top:707px;width:1200px;height:465px;background:var(--dark)}
.services .heading{position:absolute;left:0;top:30px;width:1200px;font-size:46px;color:var(--white)}
.service{position:absolute;top:118px;width:300px;text-align:center}
.service-icon{display:block;margin:0 auto}
.service-title{margin-top:30px;color:var(--blue);font-size:17px;font-weight:700}
.service-text{margin:22px auto 0;width:262px;color:var(--white);font-size:12.5px;line-height:18px}
.divider{position:absolute;top:115px;width:1px;height:320px;background:#4a4a4a}

/* about */
.about-photo{left:234px;top:1200px;width:238px;height:403px;background:linear-gradient(180deg,#f4f4f4 0%,#c4a38c 28%,#6d6d72 55%,#9c9ca0 100%)}
.about-title{left:524px;top:1215px;font-family:"Marcellus",Georgia,serif;font-size:46px;color:var(--blue);letter-spacing:1px}
.about-text{left:527px;top:1290px;width:510px;font-size:13px;line-height:19.5px;color:var(--text)}
.cta{left:534px;top:1483px;width:146px;height:41px;background:var(--black);color:var(--white);font-size:17px;font-weight:700;font-style:italic;text-align:center;line-height:37px;border:2px solid #555}

/* our work */
.work{left:0;top:1603px;width:1200px;height:466px;background:var(--blue)}
.work .heading,.team .heading{position:absolute;left:0;top:40px;width:1200px;font-size:46px}
.work .heading{color:var(--white)}
.section-sub{position:absolute;left:0;top:100px;width:1200px;text-align:center;font-size:16px}
.work .section-sub{color:var(--white)}
.work-card{position:absolute;top:173px;width:280px}
.work-image{height:155px;background:linear-gradient(135deg,#1f3f6e,#5fa6d8 55%,#d9e8f2)}
.work-label{position:relative;margin:-46px 12px 0;height:36px;background:var(--black);color:var(--white);font-size:14.5px;font-weight:700;text-align:center;line-height:36px}
.work-text{margin-top:18px;color:var(--white);font-size:12.5px;line-height:18px;text-align:center;padding:0 12px}

/* team */
.team{left:0;top:2069px;width:1200px;height:586px;background:var(--white)}
.team .heading{color:var(--ink)}
.team .section-sub{color:var(--ink);font-weight:600}
.member{position:absolute;top:179px;width:236px}
.member-photo{height:276px;background:linear-gradient(180deg,#f2f4f6 0%,#d8b9a4 30%,#8ea9c8 70%,#dfe6ec 100%)}
.member-name{height:55px;background:var(--blue);color:var(--white);font-size:15px;font-weight:700;text-align:center;line-height:55px}

/* testimonial */
.testimonial{left:0;top:2655px;width:1200px;height:317px;background:var(--darker)}
.testimonial-title{position:absolute;left:0;top:38px;width:1200px;text-align:center;font-family:"Open Sans",Arial,sans-serif;font-weight:300;font-size:33px;color:var(--blue)}
.avatar{position:absolute;left:555px;top:100px;width:90px;height:90px;border-radius:50%;border:4px solid var(--blue);background:linear-gradient(180deg,#e9e4de,#c49a7e 60%,#5b6b80)}
.quote-mark{position:absolute;top:200px;font-family:Georgia,serif;font-size:70px;color:var(--blue);line-height:1}
.quote-text{position:absolute;left:272px;top:218px;width:656px;text-align:center;color:var(--white);font-size:12.5px;line-height:19px}
.quote-name{position:absolute;left:0;top:274px;width:1200px;text-align:center;color:var(--white);font-size:14px;font-weight:700;font-style:italic}

/* footer */
.footer-bar{left:0;top:2972px;width:1200px;height:69px;background:var(--blue)}
.footer-nav{position:absolute;left:188px;top:17px;display:flex;list-style:none;gap:6px}
.footer-nav li{font-size:13px;color:var(--white);padding:0 14px;height:35px;line-height:35px;white-space:nowrap}
.footer-nav li.is-active{background:var(--black)}
.social{position:absolute;left:880px;top:20px;display:flex;gap:6px}
.social span{width:28px;height:28px;background:var(--blue-deep);border:1px solid rgba(255,255,255,.5)}
.footer-bottom{left:0;top:3041px;width:1200px;height:62px;background:var(--darker);color:var(--muted);font-size:12px;text-align:center;line-height:62px}
</style>
</head>
<body>

<div class="abs hero-photo" role="img" aria-label="Photograph of a smiling business team standing in a row"></div>

<header class="abs site-nav">
  <div class="abs site-name">MESHWORKS</div>
  <ul class="abs nav-list">
    <li>Home</li><li>What we do</li><li>News blog</li><li>Software</li><li>Our Team</li><li>Contact Us</li>
  </ul>
</header>

<div class="abs hero-caption">
  <div class="hero-title">LOREM IPSUM</div>
  <p class="hero-text">Lorem ipsum dolor sit amet, consectetur adipiscing elit, sed do eiusmod tempor incididunt ut labore et dolore magna aliqua.</p>
</div>
<div class="abs hero-arrow" style="top:590px">
  <svg width="36" height="40" viewBox="0 0 36 40"><path d="M15 14l6 6-6 6" fill="none" stroke="#fff" stroke-width="2"/></svg>
</div>
<div class="abs hero-arrow" style="top:634px">
  <svg width="36" height="40" viewBox="0 0 36 40"><path d="M21 14l-6 6 6 6" fill="none" stroke="#fff" stroke-width="2"/></svg>
</div>

<section class="abs services">
  <h2 class="heading">WHAT WE DO</h2>
  <div class="divider" style="left:440px"></div>
  <div class="divider" style="left:760px"></div>

  <div class="service" style="left:126px">
    <svg class="service-icon" width="78" height="78" viewBox="0 0 78 78">
      <circle cx="39" cy="39" r="38" fill="#3aaee3"/>
      <rect x="33" y="22" width="12" height="9" fill="#fff"/>
      <rect x="21" y="46" width="10" height="9" fill="#fff"/>
      <rect x="34" y="46" width="10" height="9" fill="#fff"/>
      <rect x="47" y="46" width="10" height="9" fill="#fff"/>
      <path d="M39 31v8M26 46v-7h26v7M39 39v7" fill="none" stroke="#fff" stroke-width="2"/>
    </svg>
    <h3 class="service-title">LOREM IPSUM DOLOR</h3>
    <p class="service-text">Lorem ipsum dolor sit amet, consectetur adipiscing elit, sed do eiusmod tempor incididunt ut labore et dolore magna aliqua. Ut enim ad minim veniam, quis nostrud exercitation ullamco laboris nisi ut aliquip ex ea commodo consequat.</p>
  </div>

  <div class="service" style="left:450px">
    <svg class="service-icon" width="78" height="78" viewBox="0 0 78 78">
      <circle cx="39" cy="39" r="38" fill="#3aaee3"/>
      <path d="M26 36a14 14 0 0 1 24-8" fill="none" stroke="#fff" stroke-width="4"/>
      <path d="M52 42a14 14 0 0 1-24 8" fill="none" stroke="#fff" stroke-width="4"/>
      <path d="M46 22l7 5-7 5z" fill="#fff"/>
      <path d="M32 56l-7-5 7-5z" fill="#fff"/>
    </svg>
    <h3 class="service-title">LOREM IPSUM DOLOR</h3>
    <p class="service-text">Lorem ipsum dolor sit amet, consectetur adipiscing elit, sed do eiusmod tempor incididunt ut labore et dolore magna aliqua. Ut enim ad minim veniam, quis nostrud exercitation ullamco laboris nisi ut aliquip ex ea commodo consequat.</p>
  </div>

  <div class="service" style="left:778px">
    <svg class="service-icon" width="78" height="78" viewBox="0 0 78 78">
      <circle cx="39" cy="39" r="38" fill="#3aaee3"/>
      <rect x="22" y="22" width="34" height="34" fill="none" stroke="#fff" stroke-width="2.5"/>
      <rect x="27" y="40" width="5" height="12" fill="#fff"/>
      <rect x="36" y="30" width="5" height="22" fill="#fff"/>
      <rect x="45" y="35" width="5" height="17" fill="#fff"/>
    </svg>
    <h3 class="service-title">LOREM IPSUM DOLOR</h3>
    <p class="service-text">Lorem ipsum dolor sit amet, consectetur adipiscing elit, sed do eiusmod tempor incididunt ut labore et dolore magna aliqua. Ut enim ad minim veniam, quis nostrud exercitation ullamco laboris nisi ut aliquip ex ea commodo consequat.</p>
  </div>
</section>

<div class="abs about-photo" role="img" aria-label="Photograph of a smiling businesswoman in a grey suit with arms crossed"></div>
<h2 class="abs about-title">LOREM IPSUM</h2>
<p class="abs about-text">Sed ut perspiciatis unde omnis iste natus error sit voluptatem accusantium doloremque laudantium, totam rem aperiam, eaque ipsa quae ab illo inventore veritatis et quasi architecto beatae vitae dicta sunt explicabo. Nemo enim ipsam voluptatem quia voluptas sit aspernatur aut odit aut fugit, sed quia consequuntur magni dolores eos qui ratione voluptatem sequi nesciunt. Neque porro quisquam est, qui dolorem ipsum quia dolor sit amet, consectetur, adipisci velit, sed quia non numquam eius modi tempora incidunt ut labore et dolore magnam aliquam quaerat voluptatem. Ut enim ad minima veniam, quis nostrum exercitationem ullam corporis suscipit laboriosam.</p>
<div class="abs cta">CLICK HERE</div>

<section class="abs work">
  <h2 class="heading">OUR WORK</h2>
  <p class="section-sub">Sed ut perspiciatis unde omnis iste natus error sit voluptatem accusantium doloremque</p>

  <div class="work-card" style="left:170px">
    <div class="work-image" role="img" aria-label="Photograph of a city skyline at dusk"></div>
    <div class="work-label">LOREM IPSUM DOLOR</div>
    <p class="work-text">Lorem ipsum dolor sit amet, consectetur adipiscing elit, sed do eiusmod tempor incididunt ut labore et dolore.</p>
  </div>
  <div class="work-card" style="left:460px">
    <div class="work-image" role="img" aria-label="Photograph of a hand touching a digital interface" style="background:linear-gradient(135deg,#0f3c66,#3f8ccc 55%,#bfe0f3)"></div>
    <div class="work-label">LOREM IPSUM DOLOR</div>
    <p class="work-text">Lorem ipsum dolor sit amet, consectetur adipiscing elit, sed do eiusmod tempor incididunt ut labore et dolore.</p>
  </div>
  <div class="work-card" style="left:750px">
    <div class="work-image" role="img" aria-label="Photograph of a group of smiling colleagues" style="background:linear-gradient(135deg,#e9e9e9,#c9a08a 50%,#5c6c84)"></div>
    <div class="work-label">LOREM IPSUM DOLOR</div>
    <p class="work-text">Lorem ipsum dolor sit amet, consectetur adipiscing elit, sed do eiusmod tempor incididunt ut labore et dolore.</p>
  </div>
</section>

<section class="abs team">
  <h2 class="heading">OUR TEAM</h2>
  <p class="section-sub">Sed ut perspiciatis unde omnis iste natus error sit voluptatem accusantium doloremque</p>

  <div class="member" style="left:196px">
    <div class="member-photo" role="img" aria-label="Portrait photograph of a team member in a light blue shirt"></div>
    <div class="member-name">LOREM IPSUM DOLOR</div>
  </div>
  <div class="member" style="left:482px">
    <div class="member-photo" role="img" aria-label="Portrait photograph of a team member in a blue shirt with arms crossed"></div>
    <div class="member-name">LOREM IPSUM DOLOR</div>
  </div>
  <div class="member" style="left:768px">
    <div class="member-photo" role="img" aria-label="Portrait photograph of a team member in a grey jacket" style="background:linear-gradient(180deg,#f2f4f6 0%,#c89e86 30%,#7d7d84 70%,#e3e5e8 100%)"></div>
    <div class="member-name">LOREM IPSUM DOLOR</div>
  </div>
</section>

<section class="abs testimonial">
  <h2 class="testimonial-title">CLIENT TESTIMONIAL</h2>
  <div class="avatar" role="img" aria-label="Portrait photograph of the client"></div>
  <span class="quote-mark" style="left:222px">&ldquo;</span>
  <span class="quote-mark" style="left:944px">&rdquo;</span>
  <p class="quote-text">Lorem ipsum dolor sit amet, consectetur adipiscing elit, sed do eiusmod tempor incididunt ut labore et dolore magna aliqua. Ut enim ad minim veniam, quis nostrud exercitation ullamco laboris nisi ut aliquip ex ea commodo consequat.</p>
  <p class="quote-name">Dorian</p>
</section>

<footer class="abs footer-bar">
  <ul class="footer-nav">
    <li class="is-active">Home</li><li>What we do</li><li>News blog</li><li>Software</li><li>Our Team</li><li>Contact Us</li>
  </ul>
  <div class="social"><span></span><span></span><span></span><span></span></div>
</footer>
<div class="abs footer-bottom">Privacy | Copyright</div>

</body>
</html>
```